Swing Dance Themed Cleaning Company Website

We need a website designed for a cleaning company based in Portland, Oregon called Foxtrot Lane. We clean homes and commercial buildings, inside and out.

needs to be vintage and like the velvet moonbeam. Speakeasy 1920s feel.
needs to be classy.

Check out foxtrotlane.com We are not happy with the site currently.

please look at house scout site for more content https://www.housescoutly.com/rated.FoxtrotLaneCleaning.41827463.html

Check out my videos on my ClipTube channel Foxtrot Lane

Target Market(s)

middle class and home owner

Industry/Entity Type

Cleaning Service

Number of Pages Required

3 page

Font styles to use
Other font styles liked:
• jazzrag

Colors

Designer to choose colors to be used in the design.

Requirements
Must have
• must be good on pc and mobile

```html
<!DOCTYPE html>
<html lang="en">
<head>
<meta charset="utf-8">
<title>Foxtrot Lane – Keep Cleaning Classy Portland</title>
<link href="https://fonts.googleapis.com/css2?family=Federo&family=Montserrat:wght@800&family=Open+Sans:wght@400;600;700&family=Roboto:wght@400;500&display=swap" rel="stylesheet">
<style>
:root{
  --yellow:#ffe100;
  --yellow-deep:#f6c800;
  --brown-light:#c27b2c;
  --brown-dark:#4e240c;
  --parchment:#efe6d1;
  --parchment-dark:#d9c7a2;
  --charcoal:#2f2e2c;
  --charcoal-card:#252422;
  --ink:#1d1d1b;
  --text:#3a3631;
  --white:#ffffff;
  --field:#3c3a14;
}
*{box-sizing:border-box;margin:0;padding:0}
html,body{width:1200px;height:2866px;overflow:hidden}
body{position:relative;font-family:"Open Sans",sans-serif;color:var(--text);background:var(--ink)}
.abs{position:absolute}
.deco{font-family:"Federo",sans-serif;text-transform:uppercase;letter-spacing:.5px}

/* hero */
.hero{left:0;top:0;width:1200px;height:690px;background:radial-gradient(ellipse at 45% 40%,var(--brown-light) 0%,#8f4d18 50%,var(--brown-dark) 100%)}
.brand{left:185px;top:36px;display:flex;align-items:center;gap:10px}
.brand-mark{width:40px;height:40px;border-radius:50%;background:var(--yellow)}
.brand-name{font-family:"Montserrat",sans-serif;font-weight:800;font-size:30px;line-height:30px;color:var(--yellow);text-transform:uppercase}
.tagline{left:183px;top:90px;font-family:"Roboto",sans-serif;font-size:12px;color:var(--yellow);text-transform:uppercase;letter-spacing:.3px}
.nav{left:487px;top:32px;display:flex;align-items:center}
.nav a{font-family:"Federo",sans-serif;text-transform:uppercase;color:var(--white);font-size:16px;text-decoration:none;margin-right:52px}
.nav a.active{background:#2a1a10;padding:10px 26px;margin-right:40px}
.hero-title{left:178px;top:216px;font-size:44px;line-height:45px;color:var(--white);font-weight:400}
.btn{display:block;background:var(--yellow);color:var(--ink);font-family:"Federo",sans-serif;text-transform:uppercase;font-size:17px;text-align:center}
.hero-btn{left:178px;top:369px;width:151px;height:44px;line-height:44px}
.dots{left:183px;top:444px;display:flex;align-items:center;gap:6px}
.dots .arrow{width:18px;height:18px;border-radius:50%;background:var(--white);display:flex;align-items:center;justify-content:center}
.dots .dot{width:7px;height:7px;border-radius:50%;background:#c9b7a2}
.dots .dot.on{background:var(--white)}
.hero-photo{left:577px;top:141px;width:432px;height:432px;border-radius:50%;border:9px solid var(--yellow);background:radial-gradient(circle at 50% 60%,#8b8f96 0%,#4d5158 55%,#2c2e33 100%)}

/* about */
.about{left:0;top:640px;width:1200px;height:580px;background:linear-gradient(180deg,var(--parchment) 0%,#e9dec6 70%,var(--parchment-dark) 100%)}
.about-art{left:153px;top:95px;width:420px;height:345px;background:radial-gradient(ellipse at center,#cfc6b3 0%,#e9e0cc 70%,rgba(233,224,204,0) 100%);border-radius:40%}
.about-title{left:588px;top:112px;font-size:36px;line-height:36px;color:var(--ink)}
.about-lead{left:588px;top:205px;font-size:15px;color:var(--text)}
.about-sub{left:588px;top:236px;font-size:18px;font-weight:600;color:var(--ink)}
.about-body{left:588px;top:270px;width:430px;font-size:15px;line-height:22px;color:var(--text)}
.about-btn{left:585px;top:359px;width:149px;height:44px;line-height:44px}

/* services */
.services{left:0;top:1220px;width:1200px;height:510px;background:radial-gradient(ellipse at center,#3b3a37 0%,var(--charcoal) 70%,#242321 100%)}
.section-title{left:0;width:1200px;text-align:center;font-size:32px}
.services .section-title{top:42px;color:var(--yellow)}
.card{width:201px;height:257px;background:var(--charcoal-card);border-radius:8px;text-align:center;color:var(--white);padding-top:28px;box-shadow:0 2px 10px rgba(0,0,0,.4)}
.card .icon{width:86px;height:86px;margin:0 auto;border-radius:50%;background:var(--yellow);display:flex;align-items:center;justify-content:center}
.card .icon span{width:70px;height:70px;border-radius:50%;border:2px solid var(--ink)}
.card h3{font-family:"Federo",sans-serif;font-weight:400;text-transform:uppercase;font-size:17px;line-height:19px;margin:14px 10px 6px}
.card p{font-size:11px;line-height:16px;color:#d8d6d0;margin:0 18px}

/* blogs */
.blogs{left:0;top:1730px;width:1200px;height:500px;background:linear-gradient(180deg,#e7dcc4 0%,var(--parchment) 40%,var(--parchment-dark) 100%)}
.blogs .section-title{top:78px;color:var(--ink)}
.post{width:262px;top:148px}
.post-photo{width:262px;height:152px}
.post-date{position:absolute;left:22px;top:136px;background:var(--yellow);color:var(--ink);font-size:13px;padding:3px 16px}
.post h4{margin-top:28px;font-size:14px;line-height:17px;font-weight:700;color:var(--ink)}
.post p{margin-top:8px;font-size:10px;line-height:13px;color:#6b655c}
.post .more{display:block;margin-top:6px;font-size:13px;font-weight:700;color:var(--ink);text-transform:uppercase}

/* contact */
.contact{left:0;top:2226px;width:1200px;height:520px;background:linear-gradient(160deg,var(--yellow) 0%,#ffd800 45%,var(--yellow-deep) 100%)}
.contact .section-title{top:50px;color:var(--ink)}
.contact-intro{left:183px;top:126px;width:320px;font-family:"Roboto",sans-serif;font-size:16px;line-height:22px;color:var(--ink)}
.info{left:180px;display:flex;gap:14px;font-family:"Roboto",sans-serif;font-size:14px;line-height:20px;color:var(--ink)}
.info strong{font-weight:500;text-transform:uppercase;display:block}
.field{background:var(--field);color:var(--white);font-family:"Roboto",sans-serif;font-size:13px;padding:10px 12px}
.submit{left:550px;top:336px;width:148px;height:44px;line-height:44px;background:var(--ink);color:var(--white);font-family:"Federo",sans-serif;text-transform:uppercase;font-size:18px;text-align:center}

/* footer */
.footer{left:0;top:2720px;width:1200px;height:146px;background:#0a0a0a}
.footer-nav{left:184px;top:56px;display:flex;gap:46px}
.footer-nav a{font-family:"Federo",sans-serif;text-transform:uppercase;color:var(--white);font-size:14px;text-decoration:none}
.copyright{left:184px;top:84px;font-size:11px;color:#bdbdbd}
.social{left:873px;top:47px;display:flex;gap:5px}
.social span{width:34px;height:34px;border-radius:50%;background:var(--white)}
.edge{position:absolute;left:0;width:1200px;display:block}
</style>
</head>
<body>

<section class="hero abs">
  <div class="brand abs"><span class="brand-mark"></span><span class="brand-name">Foxtrot Lane</span></div>
  <div class="tagline abs">Keep cleaning classy Portland</div>
  <nav class="nav abs">
    <a class="active">Home</a><a>About us</a><a>Services</a><a>Blogs</a><a>Contact us</a>
  </nav>
  <h1 class="hero-title abs deco">Commercial<br>and Residential<br>Cleaning</h1>
  <a class="hero-btn btn abs">View services</a>
  <div class="dots abs">
    <span class="arrow"><svg width="8" height="8" viewBox="0 0 8 8"><path d="M5.5 1 2.5 4l3 3" stroke="#333" stroke-width="1.6" fill="none"/></svg></span>
    <span class="dot on"></span><span class="dot"></span><span class="dot"></span><span class="dot"></span>
    <span class="arrow"><svg width="8" height="8" viewBox="0 0 8 8"><path d="M2.5 1l3 3-3 3" stroke="#333" stroke-width="1.6" fill="none"/></svg></span>
  </div>
  <div class="hero-photo abs" role="img" aria-label="Photo of a worker polishing a tiled floor with a floor machine"></div>
</section>

<section class="about abs">
  <svg class="edge" style="top:-46px" height="50" viewBox="0 0 1200 50" preserveAspectRatio="none"><path fill="#efe6d1" d="M0,50 L0,18 L35,26 L70,12 L110,22 L150,8 L190,20 L230,14 L265,28 L300,10 L345,20 L380,6 L420,18 L460,12 L500,26 L540,10 L585,22 L620,14 L660,4 L700,18 L740,12 L780,24 L820,8 L860,20 L900,14 L940,28 L980,10 L1020,22 L1060,12 L1100,24 L1140,8 L1175,20 L1200,14 L1200,50 Z"/></svg>
  <div class="about-art abs" role="img" aria-label="Illustration of a 1920s gentleman dancing with a mop"></div>
  <h2 class="about-title abs deco">About<br>Foxtrot Lane</h2>
  <p class="about-lead abs">Making the greater Portland area clean, one building at a time</p>
  <p class="about-sub abs">Good people, great service</p>
  <p class="about-body abs">Foxtrot Lane is a family owned professional cleaning business. We provide our years of cleaning experience to homes and businesses in and around Portland, Oregon.</p>
  <a class="about-btn btn abs">Read more</a>
</section>

<section class="services abs">
  <svg class="edge" style="top:-40px" height="44" viewBox="0 0 1200 44" preserveAspectRatio="none"><path fill="#302f2d" d="M0,44 L0,30 L40,22 L85,34 L120,20 L160,28 L200,16 L240,26 L280,18 L330,24 L370,12 L410,22 L450,16 L500,26 L540,10 L580,20 L620,8 L660,18 L700,6 L745,16 L790,10 L830,20 L870,8 L910,18 L950,12 L990,22 L1030,8 L1070,18 L1110,10 L1150,20 L1200,12 L1200,44 Z"/></svg>
  <h2 class="section-title abs deco">Our services</h2>
  <div class="card abs" style="left:183px;top:129px"><div class="icon" role="img" aria-label="Duster icon"><span></span></div><h3>Janitorial<br>services</h3><p>Routine janitorial, Tall cleaning, Food service sanitation, Clean room services</p></div>
  <div class="card abs" style="left:397px;top:156px"><div class="icon" role="img" aria-label="Vacuum icon"><span></span></div><h3>House cleaning</h3><p>Floors, Carpet cleaning, Refuse removal, Dusting, Interior windows, Blinds</p></div>
  <div class="card abs" style="left:611px;top:129px"><div class="icon" role="img" aria-label="Paint brush icon"><span></span></div><h3>Maintenance</h3><p>Pressure washing, Gutters, Painting, Exterior windows, Construction cleanup, Detailing</p></div>
  <div class="card abs" style="left:825px;top:156px"><div class="icon" role="img" aria-label="Light bulb icon"><span></span></div><h3>Event<br>services</h3><p>Event hosting at the oak street studio Event cleanup</p></div>
</section>

<section class="blogs abs">
  <svg class="edge" style="top:-30px" height="34" viewBox="0 0 1200 34" preserveAspectRatio="none"><path fill="#e7dcc4" d="M0,34 L0,14 L45,24 L90,8 L130,20 L175,6 L220,18 L260,10 L300,22 L345,4 L390,16 L430,8 L470,20 L515,10 L560,24 L600,8 L640,18 L685,6 L730,20 L770,12 L815,24 L860,8 L900,18 L945,10 L990,22 L1030,6 L1075,18 L1120,10 L1160,20 L1200,8 L1200,34 Z"/></svg>
  <h2 class="section-title abs deco">Our blogs</h2>
  <article class="post abs" style="left:187px">
    <div class="post-photo" role="img" aria-label="Photo of a squeegee cleaning a window" style="background:linear-gradient(135deg,#6fb6e6,#c9e4f2 60%,#b4c95a)"></div>
    <span class="post-date">02 May 2018</span>
    <h4>Praesent elementum elit at tellus nec ultricies sit amet porttito</h4>
    <p>netus et malesuada fames ac turpis egestas Cras id elit integer quis urna Ut ante enim dapibus malesuada</p>
    <span class="more">Read more</span>
  </article>
  <article class="post abs" style="left:472px">
    <div class="post-photo" role="img" aria-label="Photo of a gloved hand spraying glass cleaner" style="background:linear-gradient(135deg,#5f7a3c,#a4b27a 50%,#d9c24a)"></div>
    <span class="post-date">02 May 2018</span>
    <h4>Praesent elementum elit at tellus nec ultricies sit amet porttito</h4>
    <p>netus et malesuada fames ac turpis egestas Cras id elit integer quis urna Ut ante enim dapibus malesuada</p>
    <span class="more">Read more</span>
  </article>
  <article class="post abs" style="left:759px">
    <div class="post-photo" role="img" aria-label="Photo of a worker washing a building exterior" style="background:linear-gradient(135deg,#9ea3a6,#d6d8d8 50%,#7d8388)"></div>
    <span class="post-date">02 May 2018</span>
    <h4>Praesent elementum elit at tellus nec ultricies sit amet porttito</h4>
    <p>netus et malesuada fames ac turpis egestas Cras id elit integer quis urna Ut ante enim dapibus malesuada</p>
    <span class="more">Read more</span>
  </article>
</section>

<section class="contact abs">
  <h2 class="section-title abs deco">Contact us</h2>
  <p class="contact-intro abs">If you're ready to experience a professional cleaning, reach out to us now!</p>
  <div class="info abs" style="top:196px">
    <svg width="16" height="20" viewBox="0 0 16 20"><path d="M8 1a6 6 0 0 0-6 6c0 4.5 6 12 6 12s6-7.5 6-12a6 6 0 0 0-6-6z" fill="#1d1d1b"/><circle cx="8" cy="7" r="2.2" fill="#ffe100"/></svg>
    <div><strong>Address</strong>418 SE Alder Row #210, Portland, OR 97214</div>
  </div>
  <div class="info abs" style="top:264px">
    <svg width="16" height="18" viewBox="0 0 16 18"><path d="M3 1.5l3 .5 1 4-2 1.5a9 9 0 0 0 5 5L11.5 10.5l4 1 .5 3c-1 1.5-3 2-4.5 1.5A14 14 0 0 1 1.5 6C1 4.5 1.5 2.5 3 1.5z" fill="none" stroke="#1d1d1b" stroke-width="1.4"/></svg>
    <div><strong>Cell phone</strong>971-555-0148</div>
  </div>
  <div class="info abs" style="top:332px">
    <svg width="18" height="14" viewBox="0 0 18 14"><rect x="1" y="1" width="16" height="12" fill="none" stroke="#1d1d1b" stroke-width="1.4"/><path d="M1 1l8 6 8-6" fill="none" stroke="#1d1d1b" stroke-width="1.4"/></svg>
    <div><strong>Email</strong>maria@foxtrotlane.com</div>
  </div>
  <div class="field abs" style="left:548px;top:126px;width:230px;height:38px">First Name</div>
  <div class="field abs" style="left:787px;top:126px;width:230px;height:38px">Last Name</div>
  <div class="field abs" style="left:548px;top:172px;width:230px;height:38px">Email</div>
  <div class="field abs" style="left:787px;top:172px;width:230px;height:38px">Phone</div>
  <div class="field abs" style="left:548px;top:218px;width:469px;height:105px">Message</div>
  <div class="submit abs">Submit</div>
</section>

<footer class="footer abs">
  <svg class="edge" style="top:-34px" height="38" viewBox="0 0 1200 38" preserveAspectRatio="none"><path fill="#0a0a0a" d="M0,38 L0,16 L20,26 L40,8 L60,22 L85,12 L105,28 L130,6 L150,20 L175,14 L195,30 L220,10 L245,22 L265,4 L290,24 L315,12 L340,26 L360,8 L385,20 L410,14 L430,28 L455,6 L480,22 L500,12 L525,26 L550,10 L570,24 L595,4 L620,20 L645,12 L665,28 L690,8 L715,22 L735,14 L760,26 L785,6 L805,20 L830,12 L855,28 L875,10 L900,22 L925,4 L945,20 L970,14 L995,26 L1015,8 L1040,22 L1065,12 L1085,28 L1110,6 L1135,20 L1155,12 L1180,24 L1200,10 L1200,38 Z"/></svg>
  <nav class="footer-nav abs"><a>Home</a><a>About us</a><a>Services</a><a>Blogs</a><a>Contact us</a></nav>
  <p class="copyright abs">© 2018 Company Name &nbsp;All right reserved</p>
  <div class="social abs" aria-label="Social links"><span></span><span></span><span></span><span></span></div>
</footer>

</body>
</html>
```